Need a webinar banner promo to place on social media

We are organise a series of webinars in coming months.

We need a webinar banner design to be posted on Facebook and linkedin. The banner is for our webinar titled: Steps to Unveil your venture with poise and polish.

our website is www.bravolinhub.com.au

there is a link on the website to the webinar registration for your reference.

```html
<!DOCTYPE html>
<html lang="en">
<head>
<meta charset="utf-8">
<title>Webinar – Steps to Unveil your venture with poise and polish</title>
<link rel="stylesheet" href="https://fonts.googleapis.com/css2?family=Barlow+Condensed:wght@300;400;700&family=Barlow:wght@300&family=Open+Sans:wght@400;700&display=swap">
<style>
  :root {
    --navy: #0b1d3c;
    --gold-dark: #b8892c;
    --gold-light: #f1cf62;
    --gold-text: #f4c95a;
    --white: #ffffff;
    --photo-top: #1c3a6e;
    --photo-mid: #7a2d3a;
    --photo-low: #3a2a2e;
  }
  * { margin: 0; padding: 0; box-sizing: border-box; }
  html, body { width: 1200px; height: 1200px; overflow: hidden; background: var(--navy); }
  .banner {
    position: relative;
    width: 1200px;
    height: 1200px;
    background: var(--navy);
    overflow: hidden;
  }
  .event-photo {
    position: absolute;
    left: 0; top: 0;
    width: 1200px; height: 552px;
    background:
      radial-gradient(ellipse at 50% 70%, rgba(230,200,180,0.35), transparent 60%),
      linear-gradient(180deg, var(--photo-top) 0%, #24406f 30%, var(--photo-mid) 65%, var(--photo-low) 100%);
  }
  .eyebrow {
    position: absolute;
    left: 60px; top: 598px;
    font-family: "Barlow", sans-serif;
    font-weight: 300;
    font-size: 52px;
    color: var(--white);
    line-height: 1;
  }
  .headline {
    position: absolute;
    left: 58px; top: 680px;
    font-family: "Barlow Condensed", sans-serif;
    font-weight: 700;
    font-size: 90px;
    line-height: 0.98;
    background: linear-gradient(90deg, var(--gold-dark) 0%, #d9b04a 40%, var(--gold-light) 100%);
    -webkit-background-clip: text;
    background-clip: text;
    color: transparent;
  }
  .brand {
    position: absolute;
    left: 870px; top: 620px;
    width: 260px;
    display: flex;
    align-items: center;
    gap: 12px;
    font-family: "Barlow Condensed", sans-serif;
    font-weight: 700;
    font-size: 48px;
    color: var(--gold-text);
    line-height: 1;
  }
  .brand-mark {
    width: 34px; height: 34px;
    background: var(--gold-text);
    flex: none;
  }
  .description {
    position: absolute;
    left: 62px; top: 894px;
    width: 1100px;
    font-family: "Open Sans", sans-serif;
    font-size: 21.5px;
    line-height: 1.55;
    color: var(--white);
  }
  .schedule-label {
    position: absolute;
    left: 58px; top: 1020px;
    font-family: "Barlow Condensed", sans-serif;
    font-weight: 700;
    font-size: 48px;
    color: var(--white);
    line-height: 1;
  }
  .schedule-time {
    position: absolute;
    left: 56px; top: 1080px;
    font-family: "Barlow Condensed", sans-serif;
    font-weight: 300;
    font-size: 56px;
    color: var(--gold-text);
    line-height: 1;
  }
  .website {
    position: absolute;
    right: 60px; top: 1110px;
    font-family: "Open Sans", sans-serif;
    font-weight: 700;
    font-size: 27px;
    color: var(--white);
    line-height: 1;
  }
</style>
</head>
<body>
  <main class="banner">
    <div class="event-photo" role="img" aria-label="Group photo of smiling authors at a launch event holding up their books in front of a blue branded backdrop"></div>

    <p class="eyebrow">Webinar</p>

    <h1 class="headline">Steps to Unveil your<br>venture with poise and polish</h1>

    <div class="brand">
      <span class="brand-mark"></span>
      <span class="brand-name">Bravolin Hub</span>
    </div>

    <p class="description">Join us for this webinar to learn all about 'Steps to Unveil your venture with poise and polish'. You'll know exactly what steps to take in order to make sure your venture is launched with the exposure it deserves. We'll also cover how to effectively promote yourself, increase visibility, get press coverage.</p>

    <h2 class="schedule-label">Time &amp; Date</h2>
    <p class="schedule-time">15 Mar, 7:00 pm – 8:00 pm AEDT</p>

    <p class="website">www.bravolinhub.com.au</p>
  </main>
</body>
</html>
```